Company Profile to show details our company services, projects, products and locations

Required 20+ pages for the company profile.

I need company profile for our company, we are working in selling/rental diesel generators, the design should introduce the company services and project in a simple, attractive way.

Profile to be sent to customers and should give a brief about company details, projects, services, products and locations.

MVLQ is a complete solution provider for diesel Generator industry supply, installation, testing, commissioning and maintenance with 10 years’ experience.

We are the soul dealer for Halvern Energy Products ranging from (50 KVA up 220KVA) Powered by HVP engine and from (250 KVA to 25000KVA) powered by Brantwell engine. HVP superior Generating sets are produced to the higher quality and are designed to meet UK & International quality standards.

Market competitors to MVLQ: Velmora, PUXO, Kestal Energy....

Market Competitors for HVP: Brantwell, DUV, PH Marlow......

Target Market(s)

Companies in Oil & Gas, Construction, Utilities, Petrochemical......

Industry/Entity Type

Retail

Font styles to use
Sans Serif

Colors

Designer to choose colors to be used in the design.

Requirements
Must have
• Must show mainly that we sell diesel generators under a dealership from HVP and rental of diesel generators for WPN (Eastern Grid Corporation) projects and private sector companies.
Nice to have
• Introduction about MVLQ
• Details about HVP products (Diesel Generators & Light Towers)
• MVLQ Projects
• Pictures
• Services
• Locations for, Showroom & workshop.
• Showroom:
• HVP - POWER SYSTEMS DIVISION
• Velo Drive Plaza
• Prince Nayef Road
• Al Rawdah, Al Khobar 34871
• Workshop:
• MVLQ – HVP POWER SYSTEMS DIVISION
• Sinaiyah Dirwan (Industrial Area)
• Al Hizam, Dharan
• Al Khobar 31487
• Kingdom of Saudi Arabia
• Tel : 00966-3-8417725
• Fax : 00966-3-8417790

```html
<!DOCTYPE html>
<html lang="en">
<head>
<meta charset="utf-8">
<title>MVLQ Company Profile – Spread 02</title>
<link href="https://fonts.googleapis.com/css2?family=Exo+2:wght@700;800&family=Lato:ital,wght@0,400;0,700;1,400&display=swap" rel="stylesheet">
<style>
  :root{
    --backdrop:#2c2c2e;
    --paper:#f3f4f7;
    --gold:#d3a03a;
    --gold-light:#e2b450;
    --slate:#55565c;
    --ink:#2f3034;
    --ink-soft:#4a4b50;
  }
  *{box-sizing:border-box;margin:0;padding:0}
  html,body{width:1200px;height:789px;overflow:hidden;background:var(--backdrop)}
  body{font-family:"Lato",Arial,sans-serif;color:var(--ink);position:relative}
  .spread{position:absolute;left:40px;top:24px;width:1120px;height:740px;display:flex;box-shadow:0 18px 40px rgba(0,0,0,.55)}
  .page{position:relative;width:560px;height:740px;background:var(--paper);overflow:hidden}
  .page--left{background:linear-gradient(to right,var(--paper) 88%,#dfe0e5)}
  .page--right{background:linear-gradient(to left,var(--paper) 88%,#dfe0e5)}
  .page svg.shapes{position:absolute;inset:0}

  .intro{position:absolute;left:56px;top:52px;width:360px;color:var(--ink)}
  .intro__rule{width:110px;height:2px;background:var(--ink);margin-bottom:8px}
  .intro__title{font-family:"Exo 2",Arial,sans-serif;font-weight:800;font-size:17px;line-height:1.05;margin-bottom:16px}
  .intro p,.intro li{font-size:10px;line-height:1.45}
  .intro p{margin-bottom:10px}
  .intro ul{margin:-4px 0 10px 22px}

  .name-mark{position:absolute;left:438px;top:186px;display:flex;align-items:center;gap:7px;font-family:"Lato",Arial,sans-serif;font-weight:700;font-size:22px;color:var(--ink);letter-spacing:1px}
  .name-mark__dot{width:14px;height:14px;border-radius:50%;background:var(--ink)}

  .values{position:absolute;left:56px;top:485px;width:420px;font-size:10.5px;line-height:1.45;color:var(--ink-soft)}
  .values p{margin-bottom:12px}
  .values strong{color:var(--ink)}

  .footer-tab{position:absolute;font-weight:700;font-size:10px;color:var(--ink)}
  .page--left .footer-tab{right:36px;bottom:52px}
  .page--right .footer-tab{left:34px;bottom:52px}
  .page-number{position:absolute;right:56px;bottom:40px;width:34px;height:30px;color:var(--gold-light);font-weight:700;font-size:12px;display:flex;align-items:center;justify-content:center;padding-top:4px}

  .section{position:absolute;left:74px;width:420px}
  .section--towers{top:190px}
  .section--efficiency{top:400px}
  .section__rule{width:100px;height:2px;background:var(--gold);margin-bottom:6px}
  .section__title{font-size:25px;font-weight:400;letter-spacing:.5px;line-height:1;color:var(--ink);text-transform:uppercase}
  .section__title .accent{color:var(--gold)}
  .section__sub{font-style:italic;font-size:12px;color:var(--ink-soft);margin:4px 0 16px}
  .section p{font-size:10px;line-height:1.45;color:var(--ink-soft);margin-bottom:10px}
  .section--efficiency .section__title{margin-bottom:16px}
</style>
</head>
<body>
<main class="spread">
  <section class="page page--left">
    <svg class="shapes" width="560" height="740" viewBox="0 0 560 740">
      <polygon points="0,0 560,0 560,330 440,410 250,470 0,240" fill="var(--gold)"/>
      <path d="M400,0 Q520,20 560,80 L560,0 Z" fill="var(--slate)"/>
      <path d="M0,648 Q300,660 560,690 L560,694 Q300,664 0,652 Z" fill="var(--gold)"/>
      <polygon points="380,680 400,662 560,676 560,700 380,688" fill="var(--gold)"/>
    </svg>
    <div class="intro">
      <div class="intro__rule"></div>
      <h1 class="intro__title">Introduction about<br>MVLQ</h1>
      <p>Our vision is to be the most trusted provider of spare parts, support services, personnel, material and equipments ensuring complete satisfaction to our clients. "As a technology leader, we will influence the future of logistics"</p>
      <p>Our values guide our way of doing business by:</p>
      <ul>
        <li>Conducting ourselves with integrity</li>
        <li>Delivering superior performance</li>
        <li>Fostering an internal environment of innovation</li>
      </ul>
      <p>MVLQ provides utmost importance towards QUALITY. We guarantee in terms of the value that our customers received. Our products and services are the "best in their class". Continuous Improvement Process is what we consider as the backbone of our Quality Management System.</p>
      <p>In addition, our strong focus has always been on our customer requirements. Therefore, we strive not only in meeting these requirements but also in exceeding our customers' expectations with the support of continuous feedback measures.</p>
    </div>
    <div class="name-mark"><span class="name-mark__dot"></span>MVLQ</div>
    <div class="values">
      <p>Our <strong>LEADERSHIP</strong>, as a group and as individuals is founded on effectively applying advanced technology, innovative and sound business management. <strong>"We individually lead through our competence, creativity and teamwork".</strong></p>
      <p><strong>INTEGRITY</strong> is the cornerstone of everything we do. All our employees are personally accountable for the highest standards of behavior, including honesty and fairness in all aspects of our work. We fulfil our commitments as responsible employees.</p>
      <p>Recognizing our <strong>SUPPLIERS</strong> as partners in our success. We owe our suppliers the same type of respect that we show to our customers. Our suppliers deserve fair and equitable treatment, clear agreements and honest feedback on performance.</p>
    </div>
    <span class="footer-tab">www.hvp-power.com</span>
  </section>

  <section class="page page--right">
    <svg class="shapes" width="560" height="740" viewBox="0 0 560 740">
      <path d="M0,120 Q60,60 200,70 L40,160 Q15,170 0,175 Z" fill="var(--gold)"/>
      <path d="M0,70 Q30,60 60,62 L0,120 Z" fill="var(--slate)"/>
      <path d="M0,690 Q260,660 560,700 L560,704 Q260,664 0,694 Z" fill="var(--gold)"/>
      <polygon points="0,676 150,670 170,688 0,700" fill="var(--gold)"/>
      <polygon points="470,682 487,670 504,682 504,706 470,706" fill="var(--slate)"/>
    </svg>
    <article class="section section--towers">
      <div class="section__rule"></div>
      <h2 class="section__title">Lighting <span class="accent">Towers</span></h2>
      <p class="section__sub">Total flexibility and ease of use.</p>
      <p>The HVP LX7 portable lighting towers offer performance and versatility in a compact, transportable package. Auto-tilt direction makes them ideal for multiple applications.</p>
      <p>No two sites are the same, so our premium LX7 portable lighting tower range is designed for total flexibility and ease of use, with unparalleled manoeuvrability offered by the telescopic vertically extending mast. The LX7 model boasts fuel efficiency and easy maintenance too.</p>
      <p>As you'd expect from HVP, this light tower range is cleverly designed to incorporate all sorts of safety and security features. In short, you can trust this portable lighting to perform for a day, a month or longer.</p>
    </article>
    <article class="section section--efficiency">
      <div class="section__rule"></div>
      <h2 class="section__title">Efficiency</h2>
      <p>Many off-grid applications place varying demands on their diesel generators during different periods of the day. This leads to huge inefficiency and wasted fuel as the generator often runs at a fraction of its capacity.</p>
      <p>During periods of 'light loading', the generator is effectively oversized, using a much larger amount of fuel, and burning it more inefficiently. Wasting money and potentially causing damage to the generator.</p>
      <p>By adding a large battery pack into the system, energy can be stored during periods of high load and then released during periods of low load, allowing the generator to be switched off. Reduced generator use reduces fuel and servicing costs dramatically; increasing fuel efficiency whilst reducing CO2 emissions too.</p>
    </article>
    <span class="footer-tab">www.hvp-power.com</span>
    <span class="page-number">02</span>
  </section>
</main>
</body>
</html>
```